K&T Fire Safety Equipment Inc. needs an updated/new website design

I would like the customer to be able to see who we are, where are are, what we do and areas we cover on the first page. I would like something modern but professional. The other fire safety companies out there have very boring & unappealing websites. I want mine seem like we've got it together and to be above average in comparison. I would like the colors to go with our logo and would like to incorporate somewhere that we have been in business for over 30 years, we are family owned and operated and that we provide service to all of central Florida from Tampa to Titusville and all of Brevard county (we can take out the" all of Brevard county" but keep the " All of Central Florida from Tampa to Titusville" and just add all counties we service to the very bottom too). We are a residential and commercial fire safety equipment company. We do sales, service and installation for fire extinguishers, emergency/exit lighting, kitchen fire suppression systems, fire alarms & fire extinguisher cabinets.I have also attached some pictures that you can use to incorporate any way you would like. Here's our current website (awful I know) to get information from if needed. kandtfiresafety.example

Target Market(s)

Restaurants, hotels, vacation rental properties & small businesses. Every business is required to have a fire extinguisher and exit lighting.

Industry/Entity Type

Fire Safety

Number of Pages Required

1 page

Font styles to use
Other font styles liked:
• I'm open to your suggestions

Colors

Designer to choose colors to be used in the design.

Requirements
Must have
• I would like the customer to be able to see who we are, where are are, what we do and areas we cover on the first page. I would like the colors to go with our logo and would like to incorporate somewhere that we have been in business for over 30 years, we are family owned and operated and that we provide service to all of central Florida from Tampa to Titusville and all of Brevard county (we can take out the" all of Brevard county" but keep the " All of Central Florida from Tampa to Titusville" and just add all counties we service to the very bottom too)
Nice to have
• Modern with high quality pictures
• I love the raised logo that I added in the attachments. If you could make the logo look like that in incorporate it as one of the first things you see that would be awesome!
• I would eventually like to have a portfolio of work completed on an additional page.
Should not have
• boring outdated look

```html
<!DOCTYPE html>
<html lang="en">
<head>
<meta charset="utf-8">
<title>K&amp;T Fire Safety Equipment Inc.</title>
<link href="https://fonts.googleapis.com/css2?family=Open+Sans:wght@400;600;700&family=Lato:wght@300;400;700;900&display=swap" rel="stylesheet">
<style>
:root{
  --orange:#f7941d;
  --ink:#111;
  --text:#333;
  --dark-card:#1e1e1e;
  --band:#e9e9e9;
  --footer:#070707;
  --field:#dedede;
}
*{margin:0;padding:0;box-sizing:border-box}
html,body{width:1200px;height:3203px;overflow:hidden}
body{position:relative;background:#fff;font-family:"Lato",sans-serif;color:var(--text)}
.abs{position:absolute}

/* header */
.site-header{left:0;top:0;width:1200px;height:90px;background:#fff}
.brand{left:94px;top:22px;display:flex;align-items:center;gap:10px}
.brand-mark{width:22px;height:22px;background:var(--orange)}
.brand-name{font-family:"Lato",sans-serif;font-weight:900;font-size:17px;color:#222;line-height:1.1}
.main-nav{left:448px;top:40px;display:flex;gap:24px;font-weight:700;font-size:15px;color:#111}
.main-nav .active{color:var(--orange)}
.call{left:978px;top:14px;text-align:center;width:130px}
.call-label{font-size:22px;font-weight:700;color:#111;letter-spacing:-.3px}
.call-number{font-size:15px;font-weight:700;color:#111;margin-top:4px}

/* hero */
.hero{left:0;top:90px;width:1200px;height:515px;background:radial-gradient(ellipse at 50% 40%,#9fb8b4 0%,#6f8f8b 45%,#3d5a58 100%)}
.hero-product{left:500px;top:110px;width:170px;height:495px;background:linear-gradient(180deg,#b33a3a,#7d1f22);opacity:.55;border-radius:40px 40px 0 0}
.hero-title{left:0;top:228px;width:1200px;text-align:center;font-family:"Open Sans",sans-serif;font-weight:700;font-size:38px;color:#fff}
.hero-sub{left:0;top:283px;width:1200px;text-align:center;font-family:"Open Sans",sans-serif;font-size:22px;line-height:31px;color:#fff}
.btn{background:var(--orange);color:#fff;font-weight:700;text-transform:uppercase;display:flex;align-items:center;justify-content:center}
.hero-btn{left:515px;top:410px;width:168px;height:43px;font-size:16px}

/* section titles */
.section-title{left:0;width:1200px;text-align:center;font-family:"Open Sans",sans-serif;font-weight:700;font-size:26px;color:var(--ink)}

/* service cards */
.service-card{top:764px;width:318px;height:417px;background:var(--dark-card)}
.service-card h3{height:47px;line-height:47px;text-align:center;color:#fff;font-family:"Open Sans",sans-serif;font-weight:700;font-size:20px}
.service-media{height:188px}
.service-card p{padding:18px 14px 0;font-family:"Open Sans",sans-serif;font-weight:700;font-size:14px;line-height:21px;color:#fff}
.read-more{display:block;text-align:center;margin-top:22px;color:var(--orange);font-size:14px}
.view-all{left:515px;top:1210px;width:140px;height:37px;font-size:14px}

/* who we are */
.who{left:0;top:1341px;width:1200px;height:294px;background:var(--band)}
.who-text{left:94px;top:1432px;width:1012px;font-size:15.5px;line-height:22px;color:#444}
.who-text b{color:#333}
.who-text .link{color:var(--orange)}
.learn-more{left:515px;top:1552px;width:140px;height:36px;font-size:14px}

/* testimonials */
.quote-box{top:1798px;width:318px;height:188px;border:2px solid #e3e3e3;background:#fff;padding:14px 16px}
.quote-box::after{content:"";position:absolute;left:18px;bottom:-22px;width:20px;height:20px;background:#fff;border-right:2px solid #e3e3e3;transform:skewY(40deg)}
.quote-mark{font-family:"Open Sans",sans-serif;font-weight:700;font-size:38px;line-height:30px;color:#e0542b}
.quote-box p{margin-top:8px;font-size:16px;line-height:22px;color:#333}
.author{top:2032px;display:flex;align-items:center;gap:16px}
.avatar{width:70px;height:70px;border-radius:50%;background:linear-gradient(160deg,#6d5a4f,#2c2522)}
.author-name{color:var(--orange);font-size:15px}
.author-role{font-size:14px;color:#111;margin-top:8px}

/* contact */
.contact{left:0;top:2197px;width:1200px;height:561px;background:linear-gradient(135deg,#3b3b3b 0%,#1f1f22 50%,#2d2d30 100%)}
.contact-title{top:2237px;color:#fff}
.field{left:361px;width:478px;background:var(--field);color:#9a9a9a;font-size:14px;padding:10px 18px}
.field::after{content:"*";position:absolute;right:8px;top:6px;color:#888}
.send{left:361px;top:2656px;width:478px;height:45px;font-size:16px}

/* footer */
.site-footer{left:0;top:2855px;width:1200px;height:348px;background:var(--footer);color:#ddd}
.footer-brand{left:94px;top:2985px;display:flex;align-items:center;gap:10px}
.footer-brand .brand-name{color:#fff;font-size:17px}
.footer-col h4{font-weight:900;font-size:16px;color:#fff;text-transform:uppercase;margin-bottom:12px}
.footer-col li{list-style:none;font-size:15.5px;line-height:24px;color:#ddd;font-weight:300}
.contact-row{display:flex;align-items:flex-start;gap:14px;font-size:15.5px;line-height:24px;font-weight:300;margin-bottom:14px}
.contact-row svg{flex:none;margin-top:5px}
.contact-row .email{color:var(--orange);font-weight:700}
.footer-rule{left:0;top:3153px;width:1200px;height:1px;background:#1d1d1d}
.copyright{left:0;top:3166px;width:1200px;text-align:center;font-size:12px;color:#3a3a3a}
</style>
</head>
<body>

<header class="site-header abs">
  <div class="brand abs"><span class="brand-mark"></span><span class="brand-name">K&amp;T Fire Safety<br>Equipment Inc.</span></div>
  <nav class="main-nav abs"><span class="active">Home</span><span>Services</span><span>About Us</span><span>Testimonials</span><span>Job</span><span>Contact Us</span></nav>
  <div class="call abs"><div class="call-label">Call Now</div><div class="call-number">1-407-555-0142</div></div>
</header>

<section class="hero abs" role="img" aria-label="Red fire extinguisher mounted on a pale teal wall"></section>
<div class="hero-product abs" role="img" aria-label="Fire extinguisher"></div>
<h1 class="hero-title abs">Phasellus quis tortor vitae magna sagittis mollis</h1>
<p class="hero-sub abs">We are family owned and operated. We have been providing residential and<br>commercial fire protection to all of Central Florida for over 30 years.</p>
<div class="btn hero-btn abs">Contact Us</div>

<h2 class="section-title abs" style="top:688px">OUR SERVICES</h2>

<article class="service-card abs" style="left:94px">
  <h3>Fire Extinguishers</h3>
  <div class="service-media" role="img" aria-label="Red fire extinguisher on white" style="background:linear-gradient(180deg,#f4f4f4,#e6e6e6)"></div>
  <p>Lorem ipsum dolor sit amet, consectetur adipiscing elit. Phasellus rhoncus ultricies ultrices. Phasellus rhoncus massa vel massa iaculis, non est dapibus.Etiam cursus porta est, lobortis varius ipsum.</p>
  <span class="read-more">Read More &rarr;</span>
</article>
<article class="service-card abs" style="left:440px">
  <h3>Emergency Signage</h3>
  <div class="service-media" role="img" aria-label="Glowing red exit sign in a dark hallway" style="background:radial-gradient(ellipse at 50% 45%,#d22b2b 0%,#5a0c0f 45%,#140405 100%)"></div>
  <p>Lorem ipsum dolor sit amet, consectetur adipiscing elit. Phasellus rhoncus ultricies ultrices. Phasellus rhoncus massa vel massa iaculis, non est dapibus.Etiam cursus porta est, lobortis varius ipsum.</p>
  <span class="read-more">Read More &rarr;</span>
</article>
<article class="service-card abs" style="left:788px">
  <h3>Fire Supression System</h3>
  <div class="service-media" role="img" aria-label="Ceiling fire sprinkler head" style="background:linear-gradient(180deg,#f1f1f1,#dcdcdc)"></div>
  <p>Lorem ipsum dolor sit amet, consectetur adipiscing elit. Phasellus rhoncus ultricies ultrices. Phasellus rhoncus massa vel massa iaculis, non est dapibus.Etiam cursus porta est, lobortis varius ipsum.</p>
  <span class="read-more">Read More &rarr;</span>
</article>

<div class="btn view-all abs">View All</div>

<section class="who abs"></section>
<h2 class="section-title abs" style="top:1360px">WHO WE ARE</h2>
<p class="who-text abs"><b>We have been providing fire protection to Central Florida for over 30 years!</b>&nbsp;&nbsp;&nbsp; <b>K &amp; T Fire Safety is family owned and operated.</b> We provide quality service, professional fire protection and life safety to meet the needs of our community. <b>We provide residential and commercial fire protection to all of Brevard County and Central Florida from Tampa to Titusville.</b>&nbsp; Our staff is exceptionally knowledgeable in fire safety and protection.&nbsp; Please feel free to <span class="link">contact us</span> with any questions or concerns.</p>
<div class="btn learn-more abs">Learn More</div>

<h2 class="section-title abs" style="top:1719px">TESTIMONIALS</h2>

<div class="quote-box abs" style="left:94px"><div class="quote-mark">&ldquo;</div><p>Lorem ipsum dolor sit amet, consect adipiscing elit. Phasellus rhoncus ultricies ultrices. Phasellus rhoncus massa vel massa iaculis.</p></div>
<div class="quote-box abs" style="left:440px"><div class="quote-mark">&ldquo;</div><p>Lorem ipsum dolor sit amet, consect adipiscing elit. Phasellus rhoncus ultricies ultrices. Phasellus rhoncus massa vel massa iaculis.</p></div>
<div class="quote-box abs" style="left:788px"><div class="quote-mark">&ldquo;</div><p>Lorem ipsum dolor sit amet, consect adipiscing elit. Phasellus rhoncus ultricies ultrices. Phasellus rhoncus massa vel massa iaculis.</p></div>

<div class="author abs" style="left:94px"><div class="avatar" role="img" aria-label="Customer portrait"></div><div><div class="author-name">Aenean semper</div><div class="author-role">Vehicula</div></div></div>
<div class="author abs" style="left:440px"><div class="avatar" role="img" aria-label="Customer portrait"></div><div><div class="author-name">Aenean semper</div><div class="author-role">Vehicula</div></div></div>
<div class="author abs" style="left:788px"><div class="avatar" role="img" aria-label="Customer portrait"></div><div><div class="author-name">Aenean semper</div><div class="author-role">Vehicula</div></div></div>

<section class="contact abs" role="img" aria-label="Dark textured wall with raised company sign"></section>
<h2 class="section-title contact-title abs">GET IN TOUCH</h2>
<div class="field abs" style="top:2321px;height:42px">Name</div>
<div class="field abs" style="top:2385px;height:42px">Subject</div>
<div class="field abs" style="top:2449px;height:179px">Message</div>
<div class="btn send abs">Send</div>

<footer class="site-footer abs"></footer>
<div class="footer-brand abs"><span class="brand-mark"></span><span class="brand-name">K&amp;T Fire Safety<br>Equipment Inc.</span></div>
<div class="footer-col abs" style="left:320px;top:2902px">
  <h4>Quick Links</h4>
  <ul><li>Home</li><li>Testimonials</li><li>About Us</li><li>Jobs</li><li>Contact Us</li></ul>
</div>
<div class="footer-col abs" style="left:495px;top:2902px">
  <h4>Services</h4>
  <ul><li>Exit Lighting</li><li>Emergency Lighting</li><li>Emergency Signage</li><li>Extinguisher Signage</li><li>Battery and Bulb Replacement</li><li>Fire Extinguisher Brackets</li><li>Fire Extinguisher Vehicle Brackets</li><li>Fire Suppression Systems</li></ul>
</div>
<div class="footer-col abs" style="left:850px;top:2902px">
  <h4>Contact Us</h4>
  <div class="contact-row"><svg width="14" height="18" viewBox="0 0 14 18"><path d="M7 0C3.1 0 0 3.1 0 7c0 5 7 11 7 11s7-6 7-11c0-3.9-3.1-7-7-7zm0 9.5A2.5 2.5 0 1 1 7 4.5a2.5 2.5 0 0 1 0 5z" fill="#fff"/></svg><span>2450 Harbor Oak Ave<br>Lakeview, FL 34700, USA</span></div>
  <div class="contact-row"><svg width="15" height="15" viewBox="0 0 24 24"><path d="M6.6 10.8a15.1 15.1 0 0 0 6.6 6.6l2.2-2.2c.3-.3.7-.4 1-.2 1.1.4 2.3.6 3.6.6.6 0 1 .4 1 1V20c0 .6-.4 1-1 1A17 17 0 0 1 3 4c0-.6.4-1 1-1h3.5c.6 0 1 .4 1 1 0 1.3.2 2.5.6 3.6.1.3 0 .7-.2 1z" fill="#fff"/></svg><span>1-407-555-0187</span></div>
  <div class="contact-row"><svg width="15" height="12" viewBox="0 0 15 12"><path d="M0 0h15v12H0z" fill="#fff"/><path d="M0 0l7.5 6L15 0" stroke="#070707" stroke-width="1.5" fill="none"/></svg><span class="email">ktfiresafety@example.com</span></div>
</div>
<div class="footer-rule abs"></div>
<p class="copyright abs">&copy; 2018. K &amp; T FIRE SAFETY EQUIPMENT INC. All Rights Reserved.</p>

</body>
</html>
```